Wine Label for a White and a Red Wine from Italy

We have a very good idea of what we want with artwork. We need you to please design a 'template' with the text so we can change out the artwork from year to year. Samples are shown of what we are looking for. We are looking for options with the two basic designs. Brand name of wine is: Valora di Castegno. Both wines are in a light green Bordeaux-style bottle (note: we don't show a light green bottle in the mockup but please remember the bottle is light green). Artwork is provided. We'd like to see either the green or blue butterfly on the white wine, the red butterfly is for the red wine. Please base the design on the attached label from Brailey and/or the attached label from Chateau Mervanges.

Target Market(s)

Millennials, women

Requirements
Must have
• The artwork (butterflies) attached.
Nice to have
• Elegant, readable fonts. Please make the text so it can be changed by the printer. Please make it so the artwork can be changed too.

```html
<!DOCTYPE html>
<html lang="it">
<head>
<meta charset="utf-8">
<title>Valora di Castegno – Barrel Select Labels</title>
<link href="https://fonts.googleapis.com/css2?family=Cormorant+Garamond:ital,wght@0,400;0,500;1,400;1,600&family=Josefin+Sans:wght@300;400&display=swap" rel="stylesheet">
<style>
  :root {
    --canvas: #ffffff;
    --label: #fdfcf9;
    --ink: #1d1a18;
    --rule: #3a3330;
    --rosso-paint: #f2a51f;
    --rosso-paint-deep: #e08a12;
    --rosso-wing: #b8321c;
    --bianco-wash: #efe9dc;
    --bianco-leaf: #9cc56a;
    --bianco-wing: #2f4a35;
    --shadow: rgba(0, 0, 0, 0.28);
  }
  * { box-sizing: border-box; margin: 0; padding: 0; }
  html, body {
    width: 1200px; height: 849px; overflow: hidden;
    background: var(--canvas);
  }
  .label-sheet {
    position: relative; width: 1200px; height: 849px;
    display: flex; justify-content: center; align-items: center; gap: 110px;
  }
  .label {
    position: relative; width: 400px; height: 490px;
    background: var(--label);
    box-shadow: 14px 18px 30px var(--shadow);
    overflow: hidden;
    color: var(--ink);
    text-align: center;
  }
  .label__art {
    position: absolute; left: 28px; right: 28px; top: 118px; height: 250px;
  }
  .label--rosso .label__art {
    background:
      radial-gradient(ellipse 26% 30% at 46% 58%, var(--rosso-wing) 0%, rgba(184,50,28,0.85) 55%, rgba(184,50,28,0) 100%),
      radial-gradient(ellipse 55% 60% at 50% 48%, var(--rosso-paint-deep) 0%, var(--rosso-paint) 55%, rgba(242,165,31,0) 100%);
  }
  .label--bianco .label__art {
    background:
      radial-gradient(ellipse 22% 28% at 48% 60%, var(--bianco-wing) 0%, rgba(47,74,53,0.7) 55%, rgba(47,74,53,0) 100%),
      radial-gradient(ellipse 40% 40% at 55% 40%, var(--bianco-leaf) 0%, rgba(156,197,106,0) 100%),
      radial-gradient(ellipse 60% 60% at 50% 50%, var(--bianco-wash) 0%, rgba(239,233,220,0) 100%);
  }
  .label__brand { position: relative; padding-top: 26px; }
  .label__name {
    display: block;
    font-family: "Cormorant Garamond", serif;
    font-style: italic; font-weight: 400;
    font-size: 60px; line-height: 0.95;
  }
  .label__origin {
    display: block;
    font-family: "Cormorant Garamond", serif;
    font-size: 30px; line-height: 1.1;
  }
  .label__rule {
    width: 150px; height: 1px; background: var(--rule);
    margin: 8px auto 6px;
  }
  .label__range {
    position: relative;
    font-family: "Josefin Sans", sans-serif; font-weight: 400;
    font-size: 17px; letter-spacing: 0.22em;
  }
  .label__footer {
    position: absolute; left: 0; right: 0; bottom: 18px;
  }
  .label__variety {
    display: inline-block;
    font-family: "Cormorant Garamond", serif; font-weight: 500;
    font-size: 15px; letter-spacing: 0.08em;
    border-top: 1px solid var(--rule); border-bottom: 1px solid var(--rule);
    padding: 3px 18px 1px;
  }
  .label__vintage {
    display: block;
    font-family: "Cormorant Garamond", serif;
    font-size: 15px; letter-spacing: 0.1em; margin-top: 2px;
  }
  .label__maker {
    display: block; margin-top: 12px;
    font-family: "Josefin Sans", sans-serif; font-weight: 400;
    font-size: 8.5px; letter-spacing: 0.12em; text-transform: uppercase;
  }
  .label__region {
    display: block; margin-top: 10px;
    font-family: "Cormorant Garamond", serif;
    font-style: italic; font-weight: 600; font-size: 13px;
  }
</style>
</head>
<body>
  <main class="label-sheet">
    <article class="label label--rosso">
      <div class="label__art" role="img" aria-label="Artwork: red butterfly over a broad stroke of golden-orange paint"></div>
      <header class="label__brand">
        <span class="label__name">Valora</span>
        <span class="label__origin">di Castegno</span>
        <div class="label__rule"></div>
        <p class="label__range">BARREL SELECT</p>
      </header>
      <footer class="label__footer">
        <span class="label__variety">ROSSO</span>
        <span class="label__vintage">2018</span>
        <span class="label__maker">Artisanally crafted by Cantina Quattro Venti · Sustainably farmed</span>
        <span class="label__region">Piemonte · Italy</span>
      </footer>
    </article>

    <article class="label label--bianco">
      <div class="label__art" role="img" aria-label="Artwork: green butterfly in soft watercolour washes on cream"></div>
      <header class="label__brand">
        <span class="label__name">Valora</span>
        <span class="label__origin">di Castegno</span>
        <div class="label__rule"></div>
        <p class="label__range">BARREL SELECT</p>
      </header>
      <footer class="label__footer">
        <span class="label__variety">BIANCO</span>
        <span class="label__vintage">2018</span>
        <span class="label__maker">Artisanally crafted by Cantina Quattro Venti · Sustainably farmed</span>
        <span class="label__region">Piemonte · Italy</span>
      </footer>
    </article>
  </main>
</body>
</html>
```